Business Card Design Project

We are a tiling/bathroom renovation business based in Brisbane Australia and are looking to get a professional looking business card designed to promote ourselves.

We provide quality workmanship to upgrade/enhance peoples' homes.
Updates

Target Market(s)

Homeowners looking to renovate their bathrooms, or get tiling done. Mostly young adults to elderly who can spare several grand to upgrade their home

Industry/Entity Type

Business

Requirements
Must have
• A bold heading is a must: "Tiling Dorsey & Kell"
Must include these details: "ABN: 38 914 027 166", "BSA Licence: 5830172", "Bretta: 0419 238 571", "Lis: 0438 912 306", "Email: tilingdorseyandkell@mailbox-demo.com", "Let Us Set It Straight".

An abstract geometrical logo that's based around squares and straight lines/arrows because we are a tiling business and our slogan is "Let Us Set It Straight"
Nice to have
• I have attached an image of a logo design I got from markvista-demo.com, and the background from Cardloom-demo.com.au templates I really like together I just need the cut and paste look ironed out.

You are free to play around with different looks and feels but around the same theme as my sample. i.e. simple but striking, minimal but eye catching, or not maybe something unexpected could be perfect who knows?
Should not have
• Photorealism on a business card is a pet peeve. Too much detail for a teeny tiny business card. A Business card should stand out at a distance and you shouldn't have to squint to see it's detail.

```html
<!DOCTYPE html>
<html lang="en">
<head>
<meta charset="utf-8">
<title>Tiling Dorsey &amp; Kell — Business Card</title>
<link rel="stylesheet" href="https://fonts.googleapis.com/css2?family=Lato:wght@400;700&display=swap">
<style>
  :root {
    --stage: #2b2b2b;
    --card: #ffffff;
    --card-shade: #ececec;
    --ink: #4a4f55;
    --accent: #e9a11a;
    --band: #5d6770;
    --band-text: #dfe3e6;
    --tile-light: #f4f4f4;
    --tile-dark: #dcdcdc;
  }
  * { box-sizing: border-box; margin: 0; padding: 0; }
  html, body { width: 1200px; height: 901px; overflow: hidden; }
  body {
    background: var(--stage);
    font-family: "Lato", sans-serif;
    color: var(--ink);
    position: relative;
  }
  .card {
    position: absolute;
    left: 290px;
    width: 620px;
    height: 354px;
    background: var(--card);
    overflow: hidden;
  }
  .card--back { top: 70px; }
  .card--front { top: 470px; background: linear-gradient(180deg, var(--card) 0%, var(--card-shade) 100%); }

  .back-texture {
    position: absolute; inset: 0;
    background: linear-gradient(135deg, var(--tile-light) 0%, var(--tile-dark) 100%);
  }
  .back-brand {
    position: absolute; inset: 0;
    display: flex; flex-direction: column; align-items: center; justify-content: center;
    gap: 22px;
  }
  .brand-square {
    width: 70px; height: 70px;
    border: 6px solid var(--accent);
  }
  .brand-name {
    font-weight: 700;
    color: var(--ink);
    letter-spacing: 2px;
    text-transform: uppercase;
  }
  .back-brand .brand-name { font-size: 34px; }

  .front-brand {
    position: absolute; top: 70px; left: 0; right: 0;
    display: flex; align-items: center; justify-content: center; gap: 14px;
  }
  .front-brand .brand-square { width: 44px; height: 44px; border-width: 5px; }
  .front-brand .brand-name { font-size: 24px; }

  .reg { position: absolute; font-size: 11px; letter-spacing: 0.5px; }
  .reg--abn { left: 44px; top: 140px; }
  .reg--bsa { right: 44px; top: 38px; }

  .contact { position: absolute; font-size: 18px; }
  .contact .who { color: var(--accent); }
  .contact--lis { right: 44px; top: 170px; }
  .contact--bretta { left: 44px; top: 232px; font-size: 19px; }
  .contact--email { left: 220px; top: 208px; font-size: 14px; }

  .slogan-band {
    position: absolute; left: 0; right: 0; bottom: 0; height: 70px;
    background: var(--band);
    display: flex; align-items: center; justify-content: center;
  }
  .slogan {
    color: var(--band-text);
    font-size: 15px;
    letter-spacing: 8px;
    text-transform: uppercase;
  }
</style>
</head>
<body>
  <section class="card card--back" aria-label="Card back">
    <div class="back-texture" role="img" aria-label="Soft grey diamond tile texture"></div>
    <div class="back-brand">
      <span class="brand-square"></span>
      <span class="brand-name">Tiling Dorsey &amp; Kell</span>
    </div>
  </section>

  <section class="card card--front" aria-label="Card front">
    <p class="reg reg--bsa">BSA Licence: 5830172</p>
    <div class="front-brand">
      <span class="brand-square"></span>
      <span class="brand-name">Tiling Dorsey &amp; Kell</span>
    </div>
    <p class="reg reg--abn">ABN: 38 914 027 166</p>
    <p class="contact contact--lis"><span class="who">Lis:</span> 0438 912 306</p>
    <p class="contact contact--email">Email: tilingdorseyandkell@mailbox-demo.com</p>
    <p class="contact contact--bretta"><span class="who">Bretta:</span> 0419 238 571</p>
    <div class="slogan-band">
      <p class="slogan">Let Us Set It Straight</p>
    </div>
  </section>
</body>
</html>
```